Scrap Metal Recycling

We are looking for a simple yet bold business card. We already have the logo, please see attached. Color scheme of blue, black and white or just blue and white.

```html
<!DOCTYPE html>
<html lang="en">
<head>
<meta charset="utf-8">
<title>Ridgeway Metals Ltd. – Business Card</title>
<link href="https://fonts.googleapis.com/css2?family=Montserrat:wght@400;500;600;700&family=Open+Sans:wght@600&display=swap" rel="stylesheet">
<style>
  :root {
    --backdrop: #dfe1e0;
    --card-white: #ffffff;
    --card-mist: #e9e9ea;
    --brand-blue: #0aa6dc;
    --brand-blue-light: #7fcdeb;
    --charcoal: #55585c;
    --ink: #46494e;
    --text-muted: #55585c;
  }
  * { margin: 0; padding: 0; box-sizing: border-box; }
  html, body {
    width: 1200px;
    height: 800px;
    overflow: hidden;
    background: var(--backdrop);
    font-family: "Montserrat", sans-serif;
  }
  .canvas { position: relative; width: 1200px; height: 800px; }

  .card {
    position: absolute;
    overflow: hidden;
    box-shadow: 0 1px 3px rgba(0,0,0,0.12);
  }
  .card-art { position: absolute; inset: 0; width: 100%; height: 100%; }

  /* Front card */
  .card-front {
    left: 193px; top: 102px; width: 431px; height: 270px;
    background: linear-gradient(170deg, var(--card-mist) 0%, var(--card-white) 75%);
  }
  .front-brand {
    position: absolute; right: 20px; top: 29px;
    text-align: right;
  }
  .front-brand .brand-name {
    font-weight: 700; font-size: 14px; color: var(--ink);
    letter-spacing: 0.2px; line-height: 1;
  }
  .front-brand .brand-tagline {
    font-family: "Open Sans", sans-serif; font-weight: 600;
    font-size: 7px; letter-spacing: 2.2px; color: var(--brand-blue);
    margin-top: 5px;
  }
  .holder {
    position: absolute; left: 64px; top: 94px;
  }
  .holder-name {
    font-weight: 700; font-size: 20.5px; letter-spacing: 0.6px;
    color: var(--ink); line-height: 1; padding: 0 3px 3px 4px;
    border-bottom: 1px solid var(--brand-blue);
  }
  .holder-role {
    font-weight: 500; font-size: 10px; color: var(--ink);
    margin: 3px 0 0 6px; letter-spacing: 0.2px;
  }
  .contacts {
    position: absolute; left: 70px; top: 181px;
    list-style: none;
  }
  .contacts li {
    display: flex; align-items: center; height: 15px;
    font-size: 8.6px; color: var(--text-muted);
  }
  .contacts svg { width: 9px; height: 9px; margin-right: 7px; fill: var(--charcoal); flex: none; }

  /* Back card */
  .card-back {
    left: 567px; top: 424px; width: 441px; height: 276px;
    background: var(--card-white);
  }
  .back-brand { position: absolute; left: 45px; top: 90px; }
  .back-brand .brand-name {
    font-weight: 700; font-size: 25px; color: var(--ink); line-height: 1;
    letter-spacing: 0.3px;
  }
  .back-brand .brand-tagline {
    font-family: "Open Sans", sans-serif; font-weight: 600;
    font-size: 12px; letter-spacing: 4.3px; color: var(--brand-blue);
    margin-top: 8px;
  }
</style>
</head>
<body>
<main class="canvas">

  <section class="card card-front" aria-label="Business card front">
    <svg class="card-art" viewBox="0 0 846 529" preserveAspectRatio="none" aria-hidden="true">
      <defs>
        <linearGradient id="blue-corner-top" x1="0" y1="0" x2="1" y2="1">
          <stop offset="0" stop-color="var(--brand-blue-light)"/>
          <stop offset="0.35" stop-color="var(--brand-blue)"/>
        </linearGradient>
        <linearGradient id="blue-corner-bottom" x1="0" y1="0" x2="1" y2="1">
          <stop offset="0.55" stop-color="var(--brand-blue)"/>
          <stop offset="1" stop-color="var(--brand-blue-light)"/>
        </linearGradient>
      </defs>
      <path d="M0 0 H412 Q140 80 0 296 Z" fill="var(--charcoal)"/>
      <path d="M0 0 H300 Q95 85 0 278 Z" fill="url(#blue-corner-top)"/>
      <path d="M522 529 Q770 370 846 195 V529 Z" fill="var(--charcoal)"/>
      <path d="M598 529 Q800 380 846 205 V529 Z" fill="url(#blue-corner-bottom)"/>
    </svg>

    <div class="front-brand">
      <div class="brand-name">Ridgeway Metals Ltd.</div>
      <div class="brand-tagline">SCRAP METAL RECYCLING</div>
    </div>

    <div class="holder">
      <div class="holder-name">NAME SURNAME</div>
      <div class="holder-role">Job Position</div>
    </div>

    <ul class="contacts">
      <li>
        <svg viewBox="0 0 10 10"><path d="M5 0.5a3 3 0 0 0-3 3c0 2.3 3 6 3 6s3-3.7 3-6a3 3 0 0 0-3-3zm0 4.2a1.2 1.2 0 1 1 0-2.4 1.2 1.2 0 0 1 0 2.4z"/></svg>
        Company address line
      </li>
      <li>
        <svg viewBox="0 0 10 10"><path d="M2.2 0.6l1.5 1.8-0.8 1.3c0.6 1.3 1.7 2.4 3 3l1.3-0.8 1.8 1.5-0.9 1.7C4.6 9.1 0.9 5.4 0.5 1.5z"/></svg>
        +12 345 678 90
      </li>
      <li>
        <svg viewBox="0 0 10 10"><path d="M0.5 2h9v6h-9z M0.5 2l4.5 3.4 4.5-3.4" fill="none" stroke="var(--charcoal)" stroke-width="1.2"/></svg>
        email@yourcompany.com
      </li>
      <li>
        <svg viewBox="0 0 10 10"><g fill="none" stroke="var(--charcoal)" stroke-width="0.8"><circle cx="5" cy="5" r="4.2"/><ellipse cx="5" cy="5" rx="1.8" ry="4.2"/><path d="M0.8 5h8.4M1.5 3h7M1.5 7h7"/></g></svg>
        www.yourwebsite.com
      </li>
    </ul>
  </section>

  <section class="card card-back" aria-label="Business card back">
    <svg class="card-art" viewBox="0 0 864 540" preserveAspectRatio="none" aria-hidden="true">
      <defs>
        <linearGradient id="blue-sweep" x1="0" y1="0" x2="1" y2="1">
          <stop offset="0.5" stop-color="var(--brand-blue)"/>
          <stop offset="1" stop-color="var(--brand-blue-light)"/>
        </linearGradient>
      </defs>
      <path d="M78 540 Q640 460 864 170 V540 Z" fill="var(--charcoal)"/>
      <path d="M250 540 Q730 450 864 178 V540 Z" fill="url(#blue-sweep)"/>
    </svg>

    <div class="back-brand">
      <div class="brand-name">Ridgeway Metals Ltd.</div>
      <div class="brand-tagline">SCRAP METAL RECYCLING</div>
    </div>
  </section>

</main>
</body>
</html>
```